Flyer für eine Zahnarztpraxis
Zielgruppe
Zahnarztpraxis, Zielgruppe sind Patienten im Erwachsenenalter
Aufgabenstellung
Den Text habe ich bereits geschrieben. Es soll ein DINA4 Flyer werden, mit sechs Seiten.

```html
<!DOCTYPE html>
<html lang="de">
<head>
<meta charset="utf-8">
<title>Flyer Zahnarztpraxis Lindhoff – Vitamin D</title>
<link rel="stylesheet" href="https://fonts.googleapis.com/css2?family=Lora:ital,wght@0,500;0,600;0,700;1,400;1,500&family=Poppins:wght@300;400;500&display=swap">
<style>
  :root {
    --stage: #b4b4b4;
    --sage: #86a59f;
    --sage-dark: #6c8682;
    --sage-text: #6f938c;
    --red: #e3232b;
    --red-soft: #ee5a5f;
    --cream: #f5f2ed;
    --paper: #ffffff;
    --ink: #4a4a4a;
    --gold: #e9b43a;
    --gold-dark: #b8781c;
  }
  * { box-sizing: border-box; margin: 0; padding: 0; }
  html, body { width: 1200px; height: 1200px; overflow: hidden; }
  body {
    background: var(--stage);
    font-family: "Poppins", sans-serif;
    color: var(--ink);
    position: relative;
  }
  .flyer {
    position: absolute;
    top: 315px;
    left: 45px;
    display: flex;
    gap: 30px;
  }
  .spread { display: flex; box-shadow: 0 12px 30px rgba(0,0,0,.18); }
  .panel {
    position: relative;
    width: 270px;
    height: 570px;
    overflow: hidden;
  }
  .panel-heading {
    font-family: "Lora", serif;
    font-weight: 600;
    font-size: 20px;
    line-height: 1.15;
  }
  .body-text { font-size: 9.5px; line-height: 1.5; font-weight: 400; }
  .body-text p + p { margin-top: 12px; }

  /* Panel 1 */
  .panel-intro { background: linear-gradient(90deg, #e9e9e9 0%, #fafafa 70%, #f1f1f1 100%); }
  .panel-intro .panel-heading { color: var(--sage-text); position: absolute; top: 60px; left: 26px; right: 20px; }
  .panel-intro .body-text { position: absolute; top: 140px; left: 26px; right: 24px; }
  .capsules-photo {
    position: absolute; left: 0; right: 0; bottom: 0; height: 200px;
    background: radial-gradient(ellipse at 45% 55%, var(--gold) 0%, #d39a35 40%, #a9703d 62%, rgba(230,230,230,0) 78%);
  }

  /* Panel 2 */
  .panel-benefits { background: linear-gradient(180deg, var(--sage) 0%, var(--sage-dark) 55%, var(--sage) 100%); color: #fff; }
  .panel-benefits .panel-heading { position: absolute; top: 60px; left: 24px; right: 16px; color: #fff; }
  .benefit-list { position: absolute; top: 160px; left: 24px; right: 16px; list-style: none; }
  .benefit-item { display: flex; align-items: center; gap: 12px; margin-bottom: 16px; }
  .benefit-icon {
    width: 38px; height: 38px; border-radius: 50%; background: #fff; flex: none;
    display: flex; align-items: center; justify-content: center;
  }
  .benefit-label { font-size: 9.5px; font-weight: 300; line-height: 1.35; color: #eef3f2; }
  .quote-card {
    position: absolute; left: 20px; right: 20px; top: 390px; height: 140px;
    background: #fff; border-radius: 10px; display: flex; overflow: hidden;
  }
  .quote-text { width: 48%; padding: 14px 8px 10px 12px; color: var(--ink); font-size: 7px; line-height: 1.45; }
  .quote-signature { margin-top: 8px; width: 54px; height: 22px; background: #e4e9e8; border-radius: 3px; }
  .staff-photo { flex: 1; background: linear-gradient(180deg, #ecebea 0%, #d9d5d2 45%, #2b2b2d 100%); }
  .thought-dot { position: absolute; background: #fff; border-radius: 50%; }

  /* Panel 3 */
  .panel-teeth { background: var(--paper); }
  .panel-teeth .panel-heading { position: absolute; top: 60px; left: 24px; right: 18px; color: var(--sage-text); }
  .panel-teeth .body-text { position: absolute; top: 160px; left: 24px; right: 20px; }
  .deficit-bubble {
    position: absolute; top: 270px; left: 24px; right: 20px;
    background: var(--red); color: #fff; border-radius: 10px;
    padding: 12px 14px; font-size: 10px; font-weight: 500; line-height: 1.35;
  }
  .red-dot { position: absolute; background: var(--red); border-radius: 50%; }
  .risk-list { position: absolute; top: 360px; left: 24px; right: 18px; list-style: none; }
  .risk-item { display: flex; align-items: center; gap: 12px; margin-bottom: 18px; font-size: 9.5px; line-height: 1.35; }
  .risk-icon {
    width: 36px; height: 36px; border-radius: 50%; background: var(--red); flex: none;
    display: flex; align-items: center; justify-content: center;
  }

  /* Cover */
  .panel-cover { background: var(--cream); box-shadow: 0 12px 30px rgba(0,0,0,.2); }
  .cover-band-top { position: absolute; top: 0; left: 0; right: 0; height: 14px; background: var(--sage); }
  .practice-name {
    position: absolute; top: 42px; left: 30px; right: 20px;
    display: flex; align-items: center; gap: 10px; color: var(--sage-dark);
  }
  .practice-mark { width: 30px; height: 30px; border: 1.5px solid var(--sage-dark); border-radius: 50%; flex: none; }
  .practice-label { font-size: 11px; font-weight: 400; line-height: 1.25; letter-spacing: .04em; }
  .cover-photo { position: absolute; left: 30px; right: 18px; height: 150px; }
  .cover-photo-woman { top: 100px; background: linear-gradient(90deg, #d6d6d6 0%, #a9a9a9 45%, #7fa39c 55%, #9a9a9a 75%, #dcdcdc 100%); }
  .cover-photo-man { top: 290px; background: linear-gradient(90deg, #dadada 0%, #9b9b9b 45%, #7aa099 55%, #8f8f8f 75%, #d6d6d6 100%); }
  .question-bubble {
    position: absolute; background: var(--red-soft); color: #fff;
    font-family: "Lora", serif; font-size: 11px; line-height: 1.25;
    border-radius: 8px; padding: 8px 12px;
  }
  .question-tired { top: 215px; left: 18px; width: 130px; }
  .question-gums { top: 400px; left: 60px; width: 185px; text-align: right; }
  .cover-band-bottom {
    position: absolute; left: 0; right: 0; top: 490px; height: 48px; background: var(--sage);
    color: #fff; font-size: 10px; text-align: center; line-height: 1.35; padding-top: 9px; letter-spacing: .03em;
  }
  .cover-url { position: absolute; left: 0; right: 0; bottom: 12px; text-align: center; font-size: 8px; font-style: italic; color: var(--ink); }
</style>
</head>
<body>
<main class="flyer">
  <section class="spread">
    <article class="panel panel-intro">
      <h2 class="panel-heading">Was ist<br>Vitamin D eigentlich?</h2>
      <div class="body-text">
        <p>Vitamin D wird oft <strong>„Sonnenvitamin“</strong> genannt, weil unser Körper es größtenteils selbst bildet – wenn Sonne auf unsere Haut trifft.</p>
        <p>Doch: In unseren Breitengraden reicht die Sonnenstrahlung viele Monate im Jahr nicht aus, um genügend Vitamin D zu bilden.</p>
        <p>Das Vitamin unterstützt nicht nur Knochen und Zähne, sondern auch unser Immunsystem, Muskeln und Wohlbefinden.</p>
      </div>
      <div class="capsules-photo" role="img" aria-label="Goldgelbe Vitamin-D-Kapseln auf einem Holzlöffel"></div>
    </article>

    <article class="panel panel-benefits">
      <h2 class="panel-heading">Warum ist<br>Vitamin D so wichtig<br>für den Körper?</h2>
      <ul class="benefit-list">
        <li class="benefit-item">
          <span class="benefit-icon"><svg width="22" height="22" viewBox="0 0 22 22"><circle cx="11" cy="11" r="8" fill="none" stroke="#6c8682" stroke-width="2"/><circle cx="11" cy="11" r="3" fill="#6c8682"/></svg></span>
          <span class="benefit-label">Unterstützt ein<br>starkes Immunsystem</span>
        </li>
        <li class="benefit-item">
          <span class="benefit-icon"><svg width="22" height="22" viewBox="0 0 22 22"><line x1="6" y1="6" x2="16" y2="16" stroke="#6c8682" stroke-width="3" stroke-linecap="round"/><circle cx="5" cy="7" r="2.5" fill="#6c8682"/><circle cx="7" cy="5" r="2.5" fill="#6c8682"/><circle cx="15" cy="17" r="2.5" fill="#6c8682"/><circle cx="17" cy="15" r="2.5" fill="#6c8682"/></svg></span>
          <span class="benefit-label">Trägt zu kräftigen<br>Knochen bei</span>
        </li>
        <li class="benefit-item">
          <span class="benefit-icon"><svg width="22" height="22" viewBox="0 0 22 22"><path d="M5 5 L8 15 Q11 19 17 15 L15 9" fill="none" stroke="#6c8682" stroke-width="3" stroke-linecap="round" stroke-linejoin="round"/></svg></span>
          <span class="benefit-label">Fördert Muskelfunktion<br>und Gleichgewicht</span>
        </li>
        <li class="benefit-item">
          <span class="benefit-icon"><svg width="22" height="22" viewBox="0 0 22 22"><circle cx="12" cy="4" r="2.2" fill="#6c8682"/><path d="M11 7 L9 13 L5 18 M9 13 L13 15 L14 20 M10 9 L15 11" fill="none" stroke="#6c8682" stroke-width="2.2" stroke-linecap="round"/></svg></span>
          <span class="benefit-label">Kann Müdigkeit und<br>Antriebslosigkeit<br>entgegenwirken</span>
        </li>
      </ul>
      <figure class="quote-card">
        <blockquote class="quote-text">
          „Fehlt Vitamin D, kann das langfristig Auswirkungen auf viele Bereiche unserer Gesundheit haben – oft, ohne dass wir es sofort merken.“
          <div class="quote-signature" role="img" aria-label="Handschriftliche Unterschrift von Mara"></div>
        </blockquote>
        <div class="staff-photo" role="img" aria-label="Lächelnde Mitarbeiterin mit Brille und schwarzem Blazer"></div>
      </figure>
      <span class="thought-dot" style="left:26px;top:538px;width:14px;height:14px"></span>
      <span class="thought-dot" style="left:20px;top:557px;width:6px;height:6px"></span>
    </article>

    <article class="panel panel-teeth">
      <h2 class="panel-heading">Vitamin D und Ihre Zähne – eine starke Verbindung</h2>
      <div class="body-text">
        <p>Wussten Sie, dass Vitamin D entscheidend für gesunde Zähne ist? Es sorgt dafür, dass Kalzium im Körper optimal aufgenommen wird – und Kalzium ist der Baustoff für feste Zähne und stabilen Kieferknochen.</p>
      </div>
      <div class="deficit-bubble">Ein Mangel kann unter<br>anderem begünstigen:</div>
      <span class="red-dot" style="left:30px;top:326px;width:12px;height:12px"></span>
      <span class="red-dot" style="left:24px;top:343px;width:5px;height:5px"></span>
      <ul class="risk-list">
        <li class="risk-item"><span class="risk-icon"><svg width="20" height="20" viewBox="0 0 20 20"><circle cx="10" cy="6" r="3" fill="#fff"/><circle cx="6" cy="13" r="2.5" fill="#fff"/><circle cx="14" cy="13" r="2.5" fill="#fff"/></svg></span>Zahnfleischprobleme</li>
        <li class="risk-item"><span class="risk-icon"><svg width="20" height="20" viewBox="0 0 20 20"><path d="M4 7 Q10 3 16 7 L14 16 L10 12 L6 16 Z" fill="#fff"/></svg></span>Karies und Zahnverlust</li>
        <li class="risk-item"><span class="risk-icon"><svg width="20" height="20" viewBox="0 0 20 20"><path d="M4 8 H16 M4 12 H16" stroke="#fff" stroke-width="2.5" stroke-linecap="round"/></svg></span>Knochenabbau im Kiefer</li>
      </ul>
    </article>
  </section>

  <article class="panel panel-cover">
    <div class="cover-band-top"></div>
    <header class="practice-name">
      <span class="practice-mark"></span>
      <span class="practice-label">ZAHNARZTPRAXIS<br>LINDHOFF &amp; TEAM</span>
    </header>
    <div class="cover-photo cover-photo-woman" role="img" aria-label="Frau mit Zahnschmerzen hält sich die Wange, schwarz-weiß"></div>
    <p class="question-bubble question-tired">Fühlen Sie sich<br>oft müde?</p>
    <span class="red-dot" style="left:26px;top:262px;width:10px;height:10px;background:var(--red-soft)"></span>
    <div class="cover-photo cover-photo-man" role="img" aria-label="Mann mit schmerzverzerrtem Gesicht hält sich die Wange, schwarz-weiß"></div>
    <p class="question-bubble question-gums">Haben Sie manchmal<br>Zahnfleischprobleme<br>oder empfindliche Zähne?</p>
    <span class="red-dot" style="left:232px;top:464px;width:10px;height:10px"></span>
    <span class="red-dot" style="left:246px;top:478px;width:5px;height:5px"></span>
    <div class="cover-band-bottom">Vielleicht steckt mehr dahinter,<br>als Sie denken…</div>
    <p class="cover-url">www.zahnarztpraxis-birkenfeld-mitte.de</p>
  </article>
</main>
</body>
</html>
```